Vibrant business card design for Product person in Tech

I'm a 29 y/o female Product manager and I'd like to get a business card designed I can use when networking. I'd love something that stands out. Feel free to experiment with the use of colour, maybe geometrical elements - get creative! I work in the tech industry, so looking for a design without too much of a corporate feel. <br/><br/>The business card should have room for:<br/>Name<br/>Email address<br/>LinkedIn

Target Market(s)

Tech

Contact Information for Business Card

Name
Email
LinkedIn

Colors
faa54b
00a990
33b8a4
abd037
fbee3f
e667a6
ffcf3e
f59195

```html
<!DOCTYPE html>
<html lang="en">
<head>
<meta charset="UTF-8">
<title>Jordan Hale — Business Card</title>
<link href="https://fonts.googleapis.com/css2?family=Lato:wght@400;900&display=swap" rel="stylesheet">
<style>
  :root {
    --backdrop: #1f1f1f;
    --card: #f7f7f6;
    --ink: #111111;
    --muted: #6b6b6b;
    --body: #3a3a3a;
    --teal: #00a990;
    --mint: #33b8a4;
    --lime: #abd037;
    --yellow: #fbee3f;
    --sun: #ffcf3e;
    --orange: #faa54b;
    --pink: #e667a6;
    --coral: #f59195;
  }
  * { margin: 0; padding: 0; box-sizing: border-box; }
  html, body {
    width: 1200px;
    height: 800px;
    overflow: hidden;
    background: var(--backdrop);
  }
  .card {
    position: absolute;
    left: 75px;
    top: 100px;
    width: 1050px;
    height: 600px;
    background: var(--card);
    border-radius: 44px;
    overflow: hidden;
    font-family: "Lato", sans-serif;
  }
  .card__accent {
    position: absolute;
    left: 0;
    right: 0;
    bottom: 0;
    height: 14px;
    background: linear-gradient(90deg, var(--teal), var(--mint), var(--lime), var(--yellow), var(--sun), var(--orange), var(--coral), var(--pink));
  }
  .artwork {
    position: absolute;
    left: 60px;
    top: 50px;
    width: 430px;
    height: 500px;
    border-radius: 28px;
    background: linear-gradient(150deg, var(--mint) 0%, var(--lime) 30%, var(--sun) 55%, var(--coral) 80%, var(--pink) 100%);
    opacity: 0.85;
  }
  .identity {
    position: absolute;
    right: 110px;
    top: 285px;
    text-align: right;
  }
  .identity__name {
    font-weight: 900;
    font-size: 50px;
    color: var(--ink);
    line-height: 1.1;
  }
  .identity__role {
    font-weight: 400;
    font-size: 26px;
    color: var(--teal);
    margin-top: 6px;
  }
  .contacts {
    position: absolute;
    right: 50px;
    top: 445px;
    list-style: none;
  }
  .contacts__item {
    display: flex;
    align-items: center;
    justify-content: flex-end;
    gap: 22px;
    font-size: 28px;
    color: var(--body);
    line-height: 40px;
  }
  .contacts__icon {
    width: 26px;
    height: 26px;
    flex: none;
  }
</style>
</head>
<body>
  <div class="card">
    <div class="artwork" role="img" aria-label="Geometric line-art composition of triangles, a cube with a pill shape, a ring and chevrons"></div>

    <div class="identity">
      <h1 class="identity__name">Jordan Hale</h1>
      <p class="identity__role">Product Manager</p>
    </div>

    <ul class="contacts">
      <li class="contacts__item">+1 555 0142 880
        <svg class="contacts__icon" viewBox="0 0 24 24" fill="var(--pink)"><path d="M6.6 10.8a15 15 0 0 0 6.6 6.6l2.2-2.2c.3-.3.7-.4 1-.2 1.1.4 2.3.6 3.6.6.6 0 1 .4 1 1V20c0 .6-.4 1-1 1A17 17 0 0 1 3 4c0-.6.4-1 1-1h3.5c.6 0 1 .4 1 1 0 1.3.2 2.5.6 3.6.1.3 0 .7-.2 1z"/></svg>
      </li>
      <li class="contacts__item">hello@jordanhale.com
        <svg class="contacts__icon" viewBox="0 0 24 24" fill="none" stroke="var(--orange)" stroke-width="2.2"><rect x="2" y="5" width="20" height="14"/><polyline points="2,5 12,13 22,5"/></svg>
      </li>
      <li class="contacts__item">network/in/jordan.hale
        <svg class="contacts__icon" viewBox="0 0 24 24"><rect x="2" y="2" width="20" height="20" rx="4" fill="var(--teal)"/></svg>
      </li>
    </ul>

    <div class="card__accent"></div>
  </div>
</body>
</html>
```